Letterhead Creation

I would like to create a letterhead incorporating my family crest attached. My current letterhead with my information is also attached. I would also like to add my Paralegal Rosalind Merriweather

```html
<!DOCTYPE html>
<html lang="en">
<head>
<meta charset="utf-8">
<title>Letterhead – Law Offices of Martin R. Hollis</title>
<link href="https://fonts.googleapis.com/css2?family=Arimo:wght@400;700&display=swap" rel="stylesheet">
<style>
  :root {
    --navy: #2e2c82;
    --navy-deep: #23226b;
    --crest-tint: #d7d8ee;
    --paper: #ffffff;
    --ink: #111111;
    --backdrop: #ecebe8;
  }
  * { margin: 0; padding: 0; box-sizing: border-box; }
  html, body { width: 1200px; height: 800px; overflow: hidden; }
  body {
    background: var(--backdrop);
    font-family: 'Arimo', Arial, sans-serif;
    display: flex; align-items: center; justify-content: center;
  }
  .letterhead {
    position: relative;
    width: 566px; height: 780px;
    background: var(--paper);
    overflow: hidden;
    color: var(--ink);
  }
  .header-band {
    position: absolute; left: 0; top: 0; width: 100%; height: 66px;
    background: var(--navy);
    color: #fff;
    padding: 16px 0 0 26px;
  }
  .firm-name { font-size: 15px; font-weight: 700; letter-spacing: .4px; text-transform: uppercase; }
  .firm-address { font-size: 8.5px; font-weight: 700; margin-top: 4px; }
  .badge {
    position: absolute; width: 98px; height: 98px;
    background: var(--navy);
    transform: rotate(45deg);
    display: flex; align-items: center; justify-content: center;
  }
  .badge-inner {
    width: 66px; height: 66px; background: #fff;
    transform: rotate(-45deg);
    display: flex; align-items: center; justify-content: center;
    font-size: 10px; font-weight: 700; color: var(--navy);
    letter-spacing: .5px;
  }
  .badge--top { right: 70px; top: 10px; }
  .badge--bottom { left: 36px; bottom: -26px; }
  .crest-mark {
    position: absolute; left: 0; right: 0; top: 250px;
    text-align: center;
    font-size: 92px; font-weight: 700; letter-spacing: 6px;
    color: var(--crest-tint);
  }
  .letter-body {
    position: absolute; left: 42px; top: 100px; width: 490px;
    font-size: 9.5px; font-weight: 700; line-height: 1.22;
  }
  .block { margin-bottom: 10px; }
  .salutation { margin: 16px 0 10px; }
  .paragraph p { white-space: nowrap; line-height: 1.55; }
  .closing { margin: 16px 0 34px; }
  .footer-band {
    position: absolute; left: 0; bottom: 18px; width: 100%; height: 40px;
    background: var(--navy);
    color: #fff;
    display: flex; align-items: center; justify-content: flex-end; gap: 22px;
    padding-right: 22px;
    font-size: 10px; font-weight: 700;
  }
  .contact { display: flex; align-items: center; gap: 6px; }
  .contact svg { width: 12px; height: 12px; fill: none; stroke: #fff; stroke-width: 1.6; }
</style>
</head>
<body>
  <article class="letterhead">
    <header class="header-band">
      <div class="firm-name">Law Offices of Martin R. Hollis</div>
      <div class="firm-address">Martin Hollis Esq. 412 N. Alder Grove Rd. Fairmont, Ca 91840</div>
    </header>
    <div class="badge badge--top"><div class="badge-inner">HOLLIS</div></div>

    <div class="crest-mark" aria-hidden="true">HOLLIS</div>

    <section class="letter-body">
      <div class="block">
        Northgate Practice<br>
        Rosalind Merriweather<br>
        P: 555-302-0145<br>
        P.O. Box 000000<br>
        Ashby, CO 80211<br>
        northgatepractice.example
      </div>
      <div class="block">August 28, 2011</div>
      <div class="block">
        First Last Name<br>
        Street Address<br>
        City, State 00000
      </div>
      <div class="salutation">Dear :</div>
      <div class="paragraph">
        <p>Lorem ipsum dolor sit amet, consectetur adipiscing elit. Aenean ut ipsum eget massa fringilla</p>
        <p>Aliquam porta lectus nec mauris ornare venenatis. Vivamus non est turpis, et cursus sem.</p>
        <p>Morbi imperdiet neque vehicula nunc convallis gravida. Vestibulum iaculis pretium placerat.</p>
        <p>Morbi imperdiet neque vehicula nunc convallis gravida. Vestibulum iaculis pretium placerat.</p>
        <p>Etiam pellentesque, velit id dapibus fermentum, turpis sapien ornare dui, ac tincidunt ligula</p>
      </div>
      <div class="closing">Sincerely,</div>
      <div class="block">
        Rosalind Merriweather<br>
        northgatepractice.example<br>
        P.O. Box 000000<br>
        Ashby, CO 80211<br>
        P: (555) 302-0145
      </div>
    </section>

    <footer class="footer-band">
      <span class="contact">
        <svg viewBox="0 0 12 12"><rect x="3" y="1" width="6" height="10" rx="1"/></svg>
        (555) 214-7730
      </span>
      <span class="contact">
        <svg viewBox="0 0 12 12"><path d="M2 4c2-2 6-2 8 0l-1 2-2-1v-1H5v1L3 6z M3 7h6v3H3z"/></svg>
        (555) 214-7731
      </span>
      <span class="contact">
        <svg viewBox="0 0 12 12"><rect x="1" y="3" width="10" height="7"/><path d="M1 3l5 4 5-4"/></svg>
        martin@hollislaw.example
      </span>
    </footer>
    <div class="badge badge--bottom"><div class="badge-inner">HOLLIS</div></div>
  </article>
</body>
</html>
```